Start-up lawncare company needing marketing flyer to promote business model

Hello! We are looking for a marketing flyer design with the requirements below.

We would like the size to fit a flyer that is 6.25" X 9", Front and Back.

We need these to meet the KBMR ORTQ requirements, there are details attached for the indicias that need to be included, and where to put them on the back of the flyer.

Here's the items items we would like to have included on the flyer:
- Logo (Attached)

- I attached a snip of how our website looks, as well as how our app looks, and would like to follow that general color scheme

- References to our Fernquill App, in both Zenthra and Vorby stores, and our website (www.Fernquill.com)

- Reference to the neighborhood barometer and gets the point across that the more of their neighbors that sign up, the cheaper the price of service (Visual attached of what this barometer looks like)

- We are licensed and insured landscaping pros

- Real, instant, upfront pricing for mowing, mulching and most other services

- Sign up with a few easy steps and manage your account from our app or online

- Automated safe & secure transactions upon service completion and satisfaction

- Excellent customer service with our quality guaranteed commitment!

- Sign up now and receive 50% off your first mow!

- Veteran owned

- A portion of our proceeds go to "Rennick Dolby Foundation"

- List's out all of the services we will offer
- Mowing
- Mulching
- Aeration and Over-seeding
- Fertilization
- Shrub/Tree Trimming
- Leaf removal and yard clean up
- Accent lighting installation
- Sprinkler blow-out / Winterization
- Driveway pressure washing and sealing
- Firewood Delivery

Target Market(s)

Homeowners in large neighborhoods that need lawn care services

Industry/Entity Type

Lawn Care

Font styles to use
Sans Serif

Colors

Designer to choose colors to be used in the design.

Requirements
Must have
• Meet KBMR ORTQ requirements
• Keep a similar color scheme to our website, feel free to use bold accents to make it more eye-catching as people search through their mail
• Get the general point across that as more of their neighbors sign up with us, the cheaper their service will be

```html
<!DOCTYPE html>
<html lang="en">
<head>
<meta charset="utf-8">
<title>Fernquill Mailer – Front and Back</title>
<link href="https://fonts.googleapis.com/css2?family=Oswald:wght@500;700&family=Montserrat:wght@600;700;800&family=Roboto+Condensed:wght@400;500;700&family=Arimo:wght@400;700&display=swap" rel="stylesheet">
<style>
:root{
  --green:#23a84a;
  --green-dark:#178a3a;
  --teal:#2bb3a0;
  --blue:#233f9c;
  --blue-light:#3aa0e6;
  --grey-panel:#e3e4e6;
  --page:#eeeeee;
  --white:#ffffff;
  --ink:#222222;
}
*{box-sizing:border-box;margin:0;padding:0}
html,body{width:1200px;height:1200px;overflow:hidden;background:var(--page)}
.canvas{position:relative;width:1200px;height:1200px}
.card{position:absolute;width:761px;height:527px;background:var(--white);box-shadow:0 6px 16px rgba(0,0,0,.22);overflow:hidden}
.card--front{left:62px;top:53px}
.card--back{left:309px;top:620px}
.abs{position:absolute}

/* FRONT */
.hero{left:11px;top:11px;width:365px;height:168px;background:linear-gradient(180deg,var(--green) 0%,var(--teal) 100%)}
.hero__title{position:absolute;left:0;right:0;top:8px;text-align:center;color:var(--white);font-family:"Oswald",sans-serif;font-weight:700;white-space:nowrap}
.hero__line1{display:block;font-size:33px;line-height:36px;letter-spacing:.5px}
.hero__line2{display:block;font-size:27px;line-height:38px;letter-spacing:.2px}
.hero__pill{position:absolute;left:22px;top:94px;width:319px;height:63px;border:3px solid var(--white);border-radius:20px;display:flex;align-items:center}
.hero__pill svg{margin:0 14px 0 20px;flex:none}
.hero__pill p{font:600 14.5px/19px "Montserrat",sans-serif;color:var(--white)}

.why{left:11px;top:180px;width:365px;height:116px;background:var(--blue)}
.why__tab{position:absolute;right:0;top:0;width:120px;height:22px;background:var(--white);clip-path:polygon(0 0,100% 0,100% 100%,14% 100%);font:800 13px/22px "Montserrat",sans-serif;color:var(--blue-light);text-align:right;padding-right:26px}
.why__list{position:absolute;left:12px;top:5px;list-style:none}
.why__list li{display:flex;align-items:center;font:400 10.5px/17.6px "Roboto Condensed",sans-serif;color:var(--white)}
.why__list svg{margin-right:6px;flex:none}

.photo{left:384px;top:11px;width:366px;height:285px;background:linear-gradient(180deg,#a8c9ea 0%,#d9c9b4 40%,#7aa45a 62%,#3e8c2e 100%)}

.offer{left:11px;top:303px;width:322px;height:158px;background:linear-gradient(90deg,var(--green-dark),var(--green));clip-path:polygon(0 0,100% 0,88% 50%,100% 100%,0 100%)}
.offer__frame{position:absolute;left:0;top:8px;width:300px;height:142px;border-top:1.5px dashed var(--white);border-bottom:1.5px dashed var(--white)}
.offer__lead{position:absolute;left:11px;top:22px;font:600 20px/1 "Montserrat",sans-serif;color:var(--white)}
.offer__big{position:absolute;left:9px;top:49px;font:800 56px/1 "Montserrat",sans-serif;color:var(--white);letter-spacing:-1px}
.offer__mow{position:absolute;left:11px;top:109px;font:800 31px/1 "Montserrat",sans-serif;color:var(--white)}

.brand{display:flex;align-items:center;gap:8px;font:700 40px/1 "Oswald",sans-serif;color:var(--green-dark);white-space:nowrap}
.brand__dot{width:14px;height:14px;border-radius:50%;background:var(--blue);flex:none}
.brand--front{left:344px;top:362px}

.device{left:529px;top:187px;width:221px;height:330px;background:linear-gradient(160deg,#2a2a2a 0%,#2a2a2a 35%,#1fa35a 36%,#2b9e78 60%,#e2b99a 75%,#c99a7b 100%)}

.contact{height:47px;background:var(--blue);display:flex;align-items:center;gap:10px;padding-left:14px;font:700 23px/1 "Roboto Condensed",sans-serif;color:var(--white);letter-spacing:1.5px;white-space:nowrap}
.contact--front{left:11px;top:469px;width:518px}
.contact__web{margin-left:6px}

/* BACK */
.panel{left:11px;top:12px;width:416px;height:504px;background:var(--grey-panel)}
.services__title{left:17px;top:18px;font:700 17px/1 "Montserrat",sans-serif;color:var(--blue)}
.services__rule{left:11px;top:57px;width:416px;height:2px;background:var(--teal)}
.services__list{list-style:none;position:absolute;top:76px}
.services__list--a{left:17px}
.services__list--b{left:190px}
.services__list li{display:flex;align-items:center;gap:8px;font:500 11.5px/22.2px "Roboto Condensed",sans-serif;color:var(--blue);white-space:nowrap}
.svc-icon{width:14px;height:14px;border-radius:50%;background:var(--blue);flex:none;position:relative}
.svc-icon::after{content:"";position:absolute;left:4px;top:4px;width:6px;height:6px;border-radius:50%;background:var(--white);opacity:.85}

.save{left:11px;top:212px;width:432px;height:172px;background:linear-gradient(90deg,var(--green),#25b06a 60%,var(--teal))}
.save__l1{position:absolute;left:16px;top:6px;font:500 22px/26px "Oswald",sans-serif;color:var(--white);white-space:nowrap}
.save__l2{position:absolute;left:16px;top:30px;font:700 35px/38px "Oswald",sans-serif;color:var(--white);white-space:nowrap}
.save__l3{position:absolute;left:17px;top:70px;font:500 13.5px/17px "Oswald",sans-serif;color:var(--white);white-space:nowrap}
.save__l3 b{font-weight:700;font-size:16.5px}
.app{position:absolute;left:0;top:112px;width:288px;height:60px;background:var(--blue);clip-path:polygon(0 0,100% 0,86% 100%,0 100%)}
.app__l1{position:absolute;left:16px;top:7px;font:800 12.5px/1 "Montserrat",sans-serif;color:var(--white)}
.app__l2{position:absolute;left:16px;top:23px;font:700 9px/1 "Montserrat",sans-serif;color:var(--white)}
.app__l3{position:absolute;left:16px;top:35px;font:800 20px/1 "Montserrat",sans-serif;color:var(--blue-light)}

.ribbon{left:319px;top:196px;width:108px;height:188px}
.ribbon__banner{position:absolute;left:0;top:0;width:108px;height:118px;background:var(--blue);border-radius:14px 0 0 0;clip-path:polygon(0 0,100% 0,100% 100%,50% 88%,0 100%)}
.ribbon__head{position:absolute;left:0;right:0;top:8px;text-align:center;font:700 12px/14px "Montserrat",sans-serif;color:var(--white)}
.ribbon__frame{position:absolute;left:8px;top:40px;width:92px;height:64px;border:1.5px dotted var(--white);border-bottom:none}
.ribbon__pct{position:absolute;left:0;right:0;top:42px;text-align:center;font:800 27px/26px "Montserrat",sans-serif;color:var(--white)}
.ribbon__mow{position:absolute;left:0;right:0;top:127px;text-align:center;font:800 18px/20px "Montserrat",sans-serif;color:var(--blue)}

.meter{left:25px;top:400px;width:220px;height:58px}
.brand--back{left:318px;top:412px;font-size:22px;gap:6px}
.brand--back .brand__dot{width:11px;height:11px}
.contact--back{left:11px;top:470px;width:416px;font-size:20px;letter-spacing:1.2px;gap:8px}

.indicia{left:671px;top:321px;width:62px;height:63px;border:1px solid #555;font:400 8px/10px "Arimo",sans-serif;color:var(--ink);text-align:center;padding-top:5px}
.indicia b{font-weight:700}
.address{left:499px;top:417px;width:211px;height:84px;border:1px solid #555;font:400 12.5px/14px "Arimo",sans-serif;color:var(--ink)}
.address__route{position:absolute;right:16px;top:11px;font-size:10.5px}
.address__name{position:absolute;left:15px;top:42px}
</style>
</head>
<body>
<div class="canvas">

  <!-- FRONT -->
  <section class="card card--front">
    <div class="abs hero">
      <h1 class="hero__title"><span class="hero__line1">LANDSCAPING SERVICE</span><span class="hero__line2">RIGHT AT YOUR FINGERTIPS</span></h1>
      <div class="hero__pill">
        <svg width="30" height="30" viewBox="0 0 30 30" fill="none" stroke="#fff" stroke-width="2.2" stroke-linecap="round"><path d="M14 10a5 5 0 0 1 6 6"/><path d="M12 5a10 10 0 0 1 13 13"/><path d="M16 15 5 26"/><path d="M16 15v6M16 15h-6"/></svg>
        <p>Sign Up With a Few Easy Steps<br>And Manage Your Account<br>From Our App or Online</p>
      </div>
    </div>

    <div class="abs why">
      <div class="why__tab">WHY US ?</div>
      <ul class="why__list">
        <li><svg width="11" height="11" viewBox="0 0 11 11" fill="none" stroke="#fff" stroke-width="1.3"><rect x="1" y="1.5" width="8.5" height="8.5"/><path d="M3 5.5l2 2 5-6"/></svg>We are licensed and insured landscaping pros</li>
        <li><svg width="11" height="11" viewBox="0 0 11 11" fill="none" stroke="#fff" stroke-width="1.3"><rect x="1" y="1.5" width="8.5" height="8.5"/><path d="M3 5.5l2 2 5-6"/></svg>Real, instant, upfront pricing for mowing, mulching and most other services</li>
        <li><svg width="11" height="11" viewBox="0 0 11 11" fill="none" stroke="#fff" stroke-width="1.3"><rect x="1" y="1.5" width="8.5" height="8.5"/><path d="M3 5.5l2 2 5-6"/></svg>Automated safe &amp; secure transactions upon service completion and satisfaction</li>
        <li><svg width="11" height="11" viewBox="0 0 11 11" fill="none" stroke="#fff" stroke-width="1.3"><rect x="1" y="1.5" width="8.5" height="8.5"/><path d="M3 5.5l2 2 5-6"/></svg>Excellent customer service with our quality guaranteed commitment!</li>
        <li><svg width="11" height="11" viewBox="0 0 11 11" fill="none" stroke="#fff" stroke-width="1.3"><rect x="1" y="1.5" width="8.5" height="8.5"/><path d="M3 5.5l2 2 5-6"/></svg>Veteran owned</li>
        <li><svg width="11" height="11" viewBox="0 0 11 11" fill="none" stroke="#fff" stroke-width="1.3"><rect x="1" y="1.5" width="8.5" height="8.5"/><path d="M3 5.5l2 2 5-6"/></svg>A portion of our proceeds go to "Rennick Dolby Foundation"</li>
      </ul>
    </div>

    <div class="abs photo" role="img" aria-label="Photo of a landscaper with a green lawn mower in front of a suburban house with a neat lawn"></div>

    <div class="abs offer">
      <div class="offer__frame"></div>
      <p class="offer__lead">Sign up now and receive</p>
      <p class="offer__big">50% OFF</p>
      <p class="offer__mow">Your First Mow!</p>
    </div>

    <div class="abs brand brand--front"><span class="brand__dot"></span>Fernquill</div>

    <div class="abs device" role="img" aria-label="Photo of a hand holding a smartphone showing the Fernquill instant quote screen"></div>

    <div class="abs contact contact--front">
      <svg width="20" height="20" viewBox="0 0 24 24" fill="#fff"><path d="M6.6 10.8a15 15 0 0 0 6.6 6.6l2.2-2.2a1 1 0 0 1 1-.25 11.4 11.4 0 0 0 3.6.57 1 1 0 0 1 1 1V20a1 1 0 0 1-1 1A17 17 0 0 1 3 4a1 1 0 0 1 1-1h3.5a1 1 0 0 1 1 1c0 1.25.2 2.45.57 3.57a1 1 0 0 1-.25 1z"/></svg>
      <span>999-5555-218</span>
      <svg width="18" height="18" viewBox="0 0 24 24" fill="none" stroke="#fff" stroke-width="2"><circle cx="12" cy="12" r="9"/><path d="M3 12h18M12 3c3 3 3 15 0 18M12 3c-3 3-3 15 0 18"/></svg>
      <span class="contact__web">www.Fernquill.com</span>
    </div>
  </section>

  <!-- BACK -->
  <section class="card card--back">
    <div class="abs panel"></div>
    <h2 class="abs services__title">SERVICES WE PROVIDE</h2>
    <div class="abs services__rule"></div>
    <ul class="services__list services__list--a">
      <li><span class="svc-icon"></span>Mowing</li>
      <li><span class="svc-icon"></span>Mulching</li>
      <li><span class="svc-icon"></span>Aeration and Over-seeding</li>
      <li><span class="svc-icon"></span>Fertilization</li>
      <li><span class="svc-icon"></span>Shrub/Tree Trimming</li>
    </ul>
    <ul class="services__list services__list--b">
      <li><span class="svc-icon"></span>Leaf removal and yard clean up</li>
      <li><span class="svc-icon"></span>Accent lighting installation</li>
      <li><span class="svc-icon"></span>Sprinkler blow-out / Winterization</li>
      <li><span class="svc-icon"></span>Driveway pressure washing and sealing</li>
      <li><span class="svc-icon"></span>Firewood Delivery</li>
    </ul>

    <div class="abs save">
      <p class="save__l1">YOU COULD SAVE UP TO</p>
      <p class="save__l2">10% OFF OUR</p>
      <p class="save__l3">ALREADY LOW PRICES, AS MORE OF<br><b>YOUR NEIGHBORS SIGN UP!</b></p>
      <div class="app">
        <p class="app__l1">CHECK OUT OUR APP TODAY</p>
        <p class="app__l2">TO SEE HOW MUCH NEIGHBORS ARE</p>
        <p class="app__l3">ALREADY SAVING!</p>
      </div>
    </div>

    <div class="abs ribbon">
      <div class="ribbon__banner">
        <p class="ribbon__head">Sign up now<br>and receive</p>
        <div class="ribbon__frame"></div>
        <p class="ribbon__pct">50%<br>OFF</p>
      </div>
      <p class="ribbon__mow">Your First<br>Mow!</p>
    </div>

    <svg class="abs meter" viewBox="0 0 220 58" role="img" aria-label="Neighborhood savings meter from 5% to 10%">
      <defs><linearGradient id="meterFill" x1="0" x2="1"><stop offset="0" stop-color="#233f9c"/><stop offset=".55" stop-color="#3aa0e6"/><stop offset="1" stop-color="#23a84a"/></linearGradient></defs>
      <path d="M6 18 14 10 22 18v8H6z" fill="#233f9c"/>
      <path d="M73 14 84 4 95 14v12H73z" fill="#3aa0e6"/>
      <path d="M145 11 161 -3 177 11v15H145z" fill="#23a84a"/>
      <rect x="1" y="32" width="218" height="22" rx="11" fill="#fff"/>
      <rect x="1" y="32" width="186" height="22" rx="11" fill="url(#meterFill)"/>
      <text x="84" y="48" font-family="Montserrat, sans-serif" font-weight="700" font-size="12" fill="#fff">5%</text>
      <text x="190" y="48" font-family="Montserrat, sans-serif" font-weight="700" font-size="12" fill="#233f9c">10%</text>
    </svg>

    <div class="abs brand brand--back"><span class="brand__dot"></span>Fernquill</div>

    <div class="abs contact contact--back">
      <svg width="17" height="17" viewBox="0 0 24 24" fill="#fff"><path d="M6.6 10.8a15 15 0 0 0 6.6 6.6l2.2-2.2a1 1 0 0 1 1-.25 11.4 11.4 0 0 0 3.6.57 1 1 0 0 1 1 1V20a1 1 0 0 1-1 1A17 17 0 0 1 3 4a1 1 0 0 1 1-1h3.5a1 1 0 0 1 1 1c0 1.25.2 2.45.57 3.57a1 1 0 0 1-.25 1z"/></svg>
      <span>999-5555-218</span>
      <svg width="15" height="15" viewBox="0 0 24 24" fill="none" stroke="#fff" stroke-width="2"><circle cx="12" cy="12" r="9"/><path d="M3 12h18M12 3c3 3 3 15 0 18M12 3c-3 3-3 15 0 18"/></svg>
      <span class="contact__web">www.Fernquill.com</span>
    </div>

    <div class="abs indicia">PRSRT STD<br>ECRWSS<br>U.S. Postage<br><b>PAID</b><br>ORTQ RETAIL</div>

    <div class="abs address">
      <span class="address__route">*****************ECRWSS****</span>
      <p class="address__name">Local<br>Postal Customer</p>
    </div>
  </section>

</div>
</body>
</html>
```